Varnok Development and Management Corp. Business Card

A logo design project has been started for our Calgary-Alberta, Canada based land development and project management company. Using this logo, a clean, sleek, professional business card is to be developed (for digital or print media) representing the principals of the company (community, sustainability, and harmony).
Updates

Project Deadline Extended
Reason: Logo design recently completed.

Adobe Illustrator Vector file uploaded. Thanks, Lew

Target Market(s)

Similar business development professionals and other engineering project management personnel involved in land developemtn. Also used to as as the brand and image with both private individuals (Landowners), public officials (policy makers), and investors (banks, venture capitalists).

Industry/Entity Type

Digital

Requirements
Must have
• Open to designers opinion. Based on logo. Must have logo, and space for employee name, title, address, website, office / cell numbers.
Should not have
• No Palm trees or tropical references. Company is based in Calgary, Alberta, Canada.

```html
<!DOCTYPE html>
<html lang="en">
<head>
<meta charset="utf-8">
<title>Varnok Development and Management Corp. Business Card</title>
<link rel="stylesheet" href="https://fonts.googleapis.com/css2?family=Open+Sans:wght@400;600;700&display=swap">
<style>
  :root {
    --page-bg: #e9e6e1;
    --card-dark: #262a30;
    --card-mid: #3b4047;
    --accent-green: #a9cc3e;
    --band-grey: #5b6068;
    --text-light: #d9dce0;
    --text-muted: #9aa0a7;
    --text-dark: #2b2f35;
  }
  * { margin: 0; padding: 0; box-sizing: border-box; }
  html, body {
    width: 1200px; height: 1023px; overflow: hidden;
    background: var(--page-bg);
    font-family: "Open Sans", Arial, sans-serif;
  }
  .sheet {
    position: relative; width: 1200px; height: 1023px;
  }
  .card {
    position: absolute; left: 250px; width: 700px; height: 400px;
    border-radius: 6px; overflow: hidden;
    background: linear-gradient(135deg, var(--card-mid) 0%, var(--card-dark) 100%);
    box-shadow: 0 10px 30px rgba(0,0,0,0.28);
  }
  .card--front { top: 80px; }
  .card--back { top: 540px; }

  /* brand name */
  .brand { position: absolute; display: flex; align-items: center; gap: 14px; }
  .brand__mark { width: 22px; height: 22px; background: var(--accent-green); }
  .brand__name {
    font-weight: 700; color: var(--accent-green); letter-spacing: 4px;
  }
  .brand__tagline {
    position: absolute; color: var(--text-muted); font-size: 14px; letter-spacing: 0.3px;
  }

  .card--front .brand { left: 48px; top: 210px; }
  .card--front .brand__name { font-size: 46px; }
  .card--front .brand__tagline { left: 84px; top: 272px; }

  /* contact block */
  .person {
    position: absolute; left: 360px; top: 56px;
    font-size: 24px; color: var(--accent-green);
  }
  .person__name { font-weight: 700; }
  .person__divider { color: var(--text-muted); margin: 0 8px; font-weight: 400; }
  .person__title { font-size: 17px; color: var(--text-muted); }

  .contact-list {
    position: absolute; left: 380px; top: 108px; list-style: none;
  }
  .contact-list li {
    display: flex; align-items: center; gap: 12px;
    font-size: 15px; color: var(--text-light); line-height: 28px;
  }
  .contact-list svg { width: 16px; height: 16px; flex: none; }

  /* bottom bands */
  .band-grey {
    position: absolute; left: 0; right: 0; bottom: 46px; height: 36px;
    background: linear-gradient(180deg, rgba(255,255,255,0.08), rgba(255,255,255,0.16));
  }
  .band-address {
    position: absolute; left: 0; right: 0; bottom: 0; height: 46px;
    background: var(--accent-green);
    display: flex; align-items: center; justify-content: flex-end; padding-right: 36px;
    font-size: 15px; color: var(--text-dark);
  }

  .card--back .brand { left: 190px; top: 150px; }
  .card--back .brand__name { font-size: 64px; }
  .card--back .brand__tagline { left: 226px; top: 240px; font-size: 16px; }
</style>
</head>
<body>
<main class="sheet">
  <section class="card card--front" aria-label="Business card front">
    <div class="brand">
      <span class="brand__mark"></span>
      <span class="brand__name">VARNOK</span>
    </div>
    <p class="brand__tagline">Development and Management Corp</p>

    <p class="person">
      <span class="person__name">Martin Hale</span><span class="person__divider">|</span><span class="person__title">Director</span>
    </p>
    <ul class="contact-list">
      <li>
        <svg viewBox="0 0 16 16"><rect width="16" height="16" rx="2" fill="#a9cc3e"/><path d="M5 4l2 2-1 1c.6 1.3 1.7 2.4 3 3l1-1 2 2-1.5 1.5C7 12 4 9 3.5 5.5Z" fill="#262a30"/></svg>
        555-201-3344
      </li>
      <li>
        <svg viewBox="0 0 16 16"><rect width="16" height="16" rx="2" fill="#a9cc3e"/><rect x="5.5" y="3" width="5" height="10" rx="1" fill="#262a30"/></svg>
        555-201-7788
      </li>
      <li>
        <svg viewBox="0 0 16 16"><rect width="16" height="16" rx="2" fill="#a9cc3e"/><circle cx="8" cy="8" r="4.5" fill="none" stroke="#262a30" stroke-width="1.3"/><path d="M3.5 8h9M8 3.5v9" stroke="#262a30" stroke-width="1.1"/></svg>
        www.VarnokDevelopment.com
      </li>
      <li>
        <svg viewBox="0 0 16 16"><rect width="16" height="16" rx="2" fill="#a9cc3e"/><rect x="3" y="5" width="10" height="7" fill="none" stroke="#262a30" stroke-width="1.3"/><path d="M3 5l5 4 5-4" fill="none" stroke="#262a30" stroke-width="1.3"/></svg>
        info@varnokdevelopment.com
      </li>
    </ul>

    <div class="band-grey"></div>
    <div class="band-address">48 Birch Lane West, Ground Floor, Calgary, AB T2P 1K4</div>
  </section>

  <section class="card card--back" aria-label="Business card back">
    <div class="brand">
      <span class="brand__mark"></span>
      <span class="brand__name">VARNOK</span>
    </div>
    <p class="brand__tagline">Development and Management Corp</p>
  </section>
</main>
</body>
</html>
```